Stationary for Corwin Lattimore | ||
Business card, letterhead, with compliments slip, envelope | ||
Use same font as used in my logo | ||
Corporate Traditional Professional Simple |
[firstname] [surname] | ||
[title] | ||
1 Some Street Sometown Somewhereshire SW23 8SW |
someone@corwinlattimore.example | ||
www.corwinlattimore.example | ||
I am the sole employee at the moment. In the future, I hope to have other employees, so I will add a 'title' section later. Please bear this in mind when positioning the information. I am looking for something that is elegant, professional, minimilistic and tasteful. Please take a look at the website: http://www.corwinlattimore.example using the following credentials to log in: u/n: "pinewhisk" p/w: "pinewhisk847" Please feel free to message me for more information. Most importantly, I want the logo and other key information (like my name?) to be in silver (PMS 877 Metallic). |
I am flexible on this. I want space on my business cards for people to be able to write some information on. | ||

```html
<!DOCTYPE html>
<html lang="en">
<head>
<meta charset="utf-8">
<title>Corwin Lattimore — Stationery</title>
<link rel="stylesheet" href="https://fonts.googleapis.com/css2?family=Cinzel:wght@400&family=Cormorant+Garamond:wght@400;500&display=swap">
<style>
  :root{
    --canvas:#ffffff;
    --paper:#ffffff;
    --edge:#e2e2e4;
    --silver:#8d8d90;
    --silver-band:#a9a9ac;
    --silver-faint:#ececee;
    --ink:#7a7a7d;
    --shadow:rgba(0,0,0,.16);
  }
  *{box-sizing:border-box;margin:0;padding:0}
  html,body{width:1200px;height:703px;overflow:hidden;background:var(--canvas)}
  body{position:relative;font-family:"Cormorant Garamond",Georgia,serif;color:var(--ink)}
  .piece{position:absolute;background:var(--paper);border:1px solid var(--edge);box-shadow:0 8px 10px -8px var(--shadow);overflow:hidden}
  .band{background:var(--silver-band);border-color:var(--silver-band)}

  .wordmark{font-family:"Cinzel",Georgia,serif;font-weight:400;color:var(--silver);line-height:1;letter-spacing:.02em;display:flex;align-items:center;gap:6px}
  .wordmark .stack{display:flex;flex-direction:column;gap:2px}
  .wordmark .mark{background:var(--silver);display:block}
  .band .wordmark{color:#ffffff}
  .band .wordmark .mark{background:#ffffff}

  .emblem-faint{position:absolute;border-radius:50%;background:var(--silver-faint)}
  .fine{font-size:7px;line-height:1.35;color:var(--ink);letter-spacing:.02em}

  /* envelope back */
  .envelope-back{left:19px;top:19px;width:473px;height:150px}
  .envelope-back svg{position:absolute;left:0;top:0}

  /* envelope front */
  .envelope-front{left:19px;top:180px;width:473px;height:180px}
  .envelope-front .wordmark{position:absolute;left:18px;top:30px;font-size:13px}
  .envelope-front .return-address{position:absolute;left:246px;top:38px;border-left:1px solid var(--edge);padding-left:8px}

  /* compliments slip */
  .compliments{left:19px;top:432px;width:473px;height:216px}
  .compliments .wordmark{position:absolute;left:18px;top:22px;font-size:17px}
  .compliments .footer-address{position:absolute;left:18px;bottom:14px}

  /* letterhead */
  .letterhead{left:533px;top:19px;width:426px;height:640px}
  .letterhead .wordmark{position:absolute;left:18px;top:22px;font-size:13px}
  .letterhead .head-details{position:absolute;left:140px;top:24px}

  /* business cards */
  .card{width:192px}
  .card-front-a{left:984px;top:19px;height:104px}
  .card-front-b{left:984px;top:132px;height:104px}
  .card-back-wide{left:984px;top:263px;height:108px}
  .card-back-tall{left:963px;top:400px;width:60px;height:172px}
  .card-front-c{left:1023px;top:400px;width:153px;height:172px}
  .card .wordmark{position:absolute;font-size:10px}
  .card-front-a .wordmark{left:10px;top:22px}
  .card-front-a .contact{position:absolute;left:104px;top:10px}
  .card-front-b .wordmark{left:10px;top:14px}
  .card-front-b .contact{position:absolute;left:104px;top:10px}
  .card-back-wide .wordmark{left:50%;top:50%;transform:translate(-50%,-50%);font-size:12px}
  .card-back-tall .wordmark{left:50%;top:50%;transform:translate(-50%,-50%) rotate(-90deg);font-size:9px;white-space:nowrap}
  .card-front-c .contact{position:absolute;left:38px;top:16px}
  .card-front-c .wordmark{left:38px;top:64px}
  .contact .name{font-size:8px;font-weight:500;letter-spacing:.06em;text-transform:uppercase;color:var(--silver)}
  .contact .role{font-size:6.5px;margin-bottom:4px}
  .contact .line{font-size:6px;line-height:1.4}

  .closing-mark{position:absolute;left:1022px;top:610px;font-size:15px}
</style>
</head>
<body>

  <section class="piece envelope-back" aria-label="Envelope, reverse">
    <svg width="473" height="150" viewBox="0 0 473 150" aria-hidden="true">
      <polygon points="0,0 473,0 300,62 250,80 223,80 173,62" fill="var(--silver-band)"/>
    </svg>
  </section>

  <section class="piece envelope-front" aria-label="Envelope, front">
    <div class="wordmark"><span class="mark" style="width:9px;height:9px"></span><span class="stack"><span>Corwin</span><span>Lattimore</span></span></div>
    <p class="fine return-address">1 Some Street Sometown<br>Somewhereshire SW23 8SW</p>
    <span class="emblem-faint" style="right:16px;top:112px;width:52px;height:52px" aria-hidden="true"></span>
  </section>

  <section class="piece compliments" aria-label="With compliments slip">
    <div class="wordmark"><span class="mark" style="width:11px;height:11px"></span><span class="stack"><span>Corwin</span><span>Lattimore</span></span></div>
    <p class="fine footer-address">1 Some Street Sometown Somewhereshire SW23 8SW</p>
    <span class="emblem-faint" style="right:18px;top:118px;width:80px;height:80px" aria-hidden="true"></span>
  </section>

  <section class="piece letterhead" aria-label="Letterhead">
    <div class="wordmark"><span class="mark" style="width:9px;height:9px"></span><span class="stack"><span>Corwin</span><span>Lattimore</span></span></div>
    <p class="fine head-details">1 Some Street Sometown Somewhereshire SW23 8SW<br>t: +44 (0)20 7946 0123 &nbsp; w: www.corwinlattimore.example</p>
    <span class="emblem-faint" style="left:14px;bottom:14px;width:40px;height:40px" aria-hidden="true"></span>
  </section>

  <section class="piece card card-front-a" aria-label="Business card">
    <div class="wordmark"><span class="mark" style="width:7px;height:7px"></span><span class="stack"><span>Corwin</span><span>Lattimore</span></span></div>
    <div class="contact">
      <p class="name">Firstname Surname</p>
      <p class="role">Title</p>
      <p class="line">1 Some Street Sometown<br>Somewhereshire SW23 8SW<br>someone@corwinlattimore.example<br>www.corwinlattimore.example</p>
    </div>
  </section>

  <section class="piece card card-front-b" aria-label="Business card">
    <div class="wordmark"><span class="mark" style="width:7px;height:7px"></span><span class="stack"><span>Corwin</span><span>Lattimore</span></span></div>
    <div class="contact">
      <p class="name">Firstname Surname</p>
      <p class="role">Title</p>
      <p class="line">1 Some Street Sometown<br>Somewhereshire SW23 8SW<br>someone@corwinlattimore.example<br>www.corwinlattimore.example</p>
    </div>
  </section>

  <section class="piece card band card-back-wide" aria-label="Business card, reverse">
    <div class="wordmark"><span class="stack"><span>Corwin</span><span>Lattimore</span></span></div>
  </section>

  <section class="piece card band card-back-tall" aria-label="Business card, reverse">
    <div class="wordmark"><span>Corwin Lattimore</span></div>
  </section>

  <section class="piece card card-front-c" aria-label="Business card">
    <div class="contact">
      <p class="name">Firstname Surname</p>
      <p class="role">Title</p>
    </div>
    <div class="wordmark"><span class="mark" style="width:7px;height:7px"></span><span class="stack"><span>Corwin</span><span>Lattimore</span></span></div>
    <div class="contact" style="top:112px">
      <p class="line">1 Some Street Sometown<br>Somewhereshire SW23 8SW<br>someone@corwinlattimore.example<br>www.corwinlattimore.example</p>
    </div>
  </section>

  <div class="wordmark closing-mark"><span class="mark" style="width:10px;height:10px"></span><span class="stack"><span>Corwin</span><span>Lattimore</span></span></div>

</body>
</html>
```